KORBALT

The business want a professional looking business card. We have a scetch we will add but want the extra upgrade, and would like more suggestions for variations of our business cards.

```html
<!DOCTYPE html>
<html lang="en">
<head>
<meta charset="UTF-8">
<title>KORBALT Business Card</title>
<link rel="stylesheet" href="https://fonts.googleapis.com/css2?family=Playfair+Display:wght@700&family=Montserrat:wght@400;500&display=swap">
<style>
  :root {
    --bg: #2a2a2b;
    --card: #121213;
    --card-edge: #1c1c1d;
    --gold: #c9a04a;
    --gold-soft: #a98436;
    --white: #f2f2f2;
  }
  * { margin: 0; padding: 0; box-sizing: border-box; }
  html, body { width: 1200px; height: 900px; overflow: hidden; }
  body {
    background: var(--bg);
    display: flex;
    flex-direction: column;
    align-items: center;
    justify-content: center;
    gap: 40px;
  }
  .card {
    width: 700px;
    height: 400px;
    background: var(--card);
    border-radius: 30px;
    border: 1px solid var(--card-edge);
    box-shadow: 0 14px 30px rgba(0,0,0,0.45);
    position: relative;
  }
  .brand {
    display: flex;
    flex-direction: column;
    align-items: center;
  }
  .brand-row { display: flex; align-items: center; gap: 16px; }
  .brand-dot { border-radius: 50%; background: var(--gold); }
  .brand-name {
    font-family: "Playfair Display", serif;
    font-weight: 700;
    color: var(--gold);
    letter-spacing: 0.04em;
  }
  .brand-since {
    font-family: "Montserrat", sans-serif;
    font-weight: 500;
    color: var(--gold);
    letter-spacing: 0.5em;
  }

  /* Front */
  .card-front { display: flex; align-items: center; justify-content: center; }
  .card-front .brand-name { font-size: 70px; }
  .card-front .brand-dot { width: 34px; height: 34px; }
  .card-front .brand-since { font-size: 16px; margin-top: 10px; }

  /* Back */
  .card-back { display: flex; align-items: center; padding: 0 50px; }
  .card-back .brand { width: 250px; }
  .card-back .brand-name { font-size: 38px; }
  .card-back .brand-dot { width: 18px; height: 18px; }
  .card-back .brand-since { font-size: 10px; margin-top: 8px; }
  .divider { width: 1.5px; height: 170px; background: var(--gold-soft); margin: 0 36px 0 20px; }
  .person-name {
    font-family: "Playfair Display", serif;
    font-weight: 700;
    font-size: 32px;
    color: var(--gold);
    white-space: nowrap;
  }
  .person-title {
    font-family: "Montserrat", sans-serif;
    font-size: 16px;
    color: var(--white);
    margin: 4px 0 22px;
  }
  .contact-list { list-style: none; }
  .contact-item {
    display: flex; align-items: center; gap: 10px;
    font-family: "Montserrat", sans-serif;
    font-size: 16px;
    color: var(--white);
    margin-bottom: 8px;
  }
  .contact-icon { width: 15px; height: 15px; flex: none; }
</style>
</head>
<body>
  <section class="card card-front">
    <div class="brand">
      <div class="brand-row">
        <span class="brand-dot"></span>
        <span class="brand-name">KORBALT</span>
      </div>
      <span class="brand-since">SINCE 2026</span>
    </div>
  </section>

  <section class="card card-back">
    <div class="brand">
      <div class="brand-row">
        <span class="brand-dot"></span>
        <span class="brand-name">KORBALT</span>
      </div>
      <span class="brand-since">SINCE 2026</span>
    </div>
    <div class="divider"></div>
    <div class="person">
      <p class="person-name">Lars Henrik Solvang</p>
      <p class="person-title">CEO &amp; Founder</p>
      <ul class="contact-list">
        <li class="contact-item">
          <svg class="contact-icon" viewBox="0 0 16 16"><path fill="#c9a04a" d="M3.5 1.5l2.5 0 1.2 3.2-1.7 1.2c.8 1.8 2.2 3.2 4 4l1.2-1.7 3.2 1.2v2.5c0 .9-.7 1.6-1.6 1.6C6.8 13.5 2.5 9.2 1.9 3.1c0-.9.7-1.6 1.6-1.6z"/></svg>
          <span>004791234567</span>
        </li>
        <li class="contact-item">
          <svg class="contact-icon" viewBox="0 0 16 16"><rect x="1" y="3" width="14" height="10" rx="1" fill="#c9a04a"/><path d="M1.5 3.5L8 9l6.5-5.5" fill="none" stroke="#121213" stroke-width="1.3"/></svg>
          <span>korbalt.llc@mailbox.com</span>
        </li>
        <li class="contact-item">
          <svg class="contact-icon" viewBox="0 0 16 16"><circle cx="8" cy="8" r="6.5" fill="none" stroke="#c9a04a" stroke-width="1.5"/><ellipse cx="8" cy="8" rx="2.8" ry="6.5" fill="none" stroke="#c9a04a" stroke-width="1.2"/><path d="M1.5 8h13" stroke="#c9a04a" stroke-width="1.2"/></svg>
          <span>www.korbalt.llc</span>
        </li>
      </ul>
    </div>
  </section>
</body>
</html>
```